Modern Label for cleaning products for the brand Dorvalix

We need a label design for our line of cleaning products. The label should feature our logo and an image to identify the product's intended use. I've added our logo and an image for use. This only concerns the design of the label on the front of the bottle.

Label dimensions:
Label 1 (500ml bottle with spray): width 58mm x height 115mm
Label 2: (1L bottle): width 73mm x height 140mm
The design must be consistent for both bottles which you find in the pictures.

The bottles to be labeled are white. See the attachment for a photo of the bottles.

The photo must also appear on the label to identify the product's intended use.

Product information:
Brand: Dorvalix
Product: Sanitary Cleaner

This text must be placed on the label:
"Cleans, descales & freshens. followed with this text: "Ideal for quick and powerful cleaning. A ready-to-use product for everyday use."

- Mention the seperate USP's: Sanitary, Bathroom, Toilet, Wet areas

Appearance: This is a consumer product, but it must have a professional appearance. We would like to see a design that use the color blue from our logo.

Target Market(s)

Consumers who take care of their homes and want to maintain it the correct (professional) way

Font styles to use
Sans Serif

Colors
0054AA
0677BA
7BADD7
CADEEF
E8F1F8

Requirements
Must have
• USP's + use of image and logo + blend in 1 design
Nice to have
• Keep the color of the logo in the design
Should not have
• Comic sans

```html
<!DOCTYPE html>
<html lang="en">
<head>
<meta charset="utf-8">
<title>Dorvalix Sanitary Cleaner – Label Set</title>
<link rel="stylesheet" href="https://fonts.googleapis.com/css2?family=Anton&family=Poppins:wght@500;600;700&family=Roboto+Condensed:wght@700;800&display=swap">
<style>
  :root{
    --blue-deep:#0054AA;
    --blue-mid:#0677BA;
    --blue-soft:#7BADD7;
    --blue-pale:#CADEEF;
    --blue-mist:#E8F1F8;
    --navy:#10265a;
    --accent:#e0451f;
    --white:#ffffff;
    --stage:#d3e1ec;
  }
  *{box-sizing:border-box;margin:0;padding:0}
  html,body{width:1200px;height:1200px;overflow:hidden}
  body{
    background:var(--stage);
    font-family:"Poppins",sans-serif;
    display:flex;align-items:center;justify-content:center;gap:80px;
  }
  .label{
    position:relative;overflow:hidden;
    background:linear-gradient(180deg,var(--white) 55%,var(--blue-mist) 100%);
    border-radius:22px;
  }
  .label--1l{width:470px;height:900px;font-size:10px}
  .label--500{width:374px;height:740px;font-size:8px}

  .label__panel{position:absolute;inset:0;width:100%;height:100%}

  .label__ribbon{
    position:absolute;top:5.5em;left:-5em;width:22em;
    transform:rotate(-45deg);
    background:var(--navy);color:var(--white);
    font-family:"Anton",sans-serif;font-size:1em;
    text-align:center;letter-spacing:.08em;
    padding:.5em 0;
  }
  .label__ribbon span{font-size:2.4em;line-height:1}

  .brand{
    position:absolute;top:7%;right:9%;
    display:flex;align-items:center;gap:.8em;
  }
  .brand__name{color:var(--white);font-weight:600;font-size:2.8em;letter-spacing:.01em}
  .brand__dot{width:3.6em;height:3.6em;border-radius:50%;background:var(--blue-soft)}

  .claims{position:absolute;top:20%;left:12%;right:6%;color:var(--white);line-height:.95}
  .claims__small{font-family:"Anton",sans-serif;font-size:3em;letter-spacing:.06em;color:var(--blue-pale)}
  .claims__main{font-family:"Anton",sans-serif;font-size:9.2em;letter-spacing:.01em;text-shadow:0 .06em 0 var(--navy)}
  .claims__sub{font-family:"Anton",sans-serif;font-size:6.4em;letter-spacing:.02em;color:var(--blue-mist);text-shadow:0 .06em 0 var(--navy)}

  .label__visual{
    position:absolute;left:0;top:49%;width:62%;height:22%;
    border-radius:0 45% 40% 0;
    background:radial-gradient(ellipse at 55% 55%,var(--white) 0%,var(--blue-mist) 45%,var(--blue-pale) 80%,var(--blue-soft) 100%);
  }

  .usps{
    position:absolute;top:60%;left:54%;list-style:none;
    font-family:"Roboto Condensed",sans-serif;font-weight:800;
    color:var(--accent);font-size:2.6em;line-height:1.35;
  }
  .usps li{display:flex;align-items:center;gap:.45em}
  .usps li::before{content:"";width:.3em;height:.3em;border-radius:50%;background:var(--blue-deep)}

  .volume{
    position:absolute;top:82.5%;left:7%;
    background:var(--accent);color:var(--white);
    font-weight:700;font-size:2.2em;
    border-radius:.35em;padding:.15em .55em;
  }
  .label--500 .volume{font-size:1.6em;padding:.35em .5em}

  .tagline{
    position:absolute;top:82.5%;left:33%;right:5%;
    color:var(--navy);font-weight:600;font-size:1.45em;line-height:1.4;
  }

  .label__water{position:absolute;left:0;bottom:0;width:100%;height:12%}
</style>
</head>
<body>

<article class="label label--1l" aria-label="Dorvalix sanitary cleaner, 1 litre label">
  <svg class="label__panel" viewBox="0 0 100 100" preserveAspectRatio="none" aria-hidden="true">
    <defs>
      <linearGradient id="panelBlue1" x1="0" y1="0" x2="1" y2="1">
        <stop offset="0" stop-color="var(--blue-deep)"/>
        <stop offset=".6" stop-color="var(--blue-mid)"/>
        <stop offset="1" stop-color="var(--blue-deep)"/>
      </linearGradient>
    </defs>
    <path d="M0 0H100V42C80 48 50 52 0 72Z" fill="url(#panelBlue1)"/>
    <path d="M0 74C40 55 75 50 100 44V48C75 53 40 58 0 78Z" fill="var(--blue-pale)"/>
    <path d="M0 70C45 52 78 47 100 41" stroke="var(--white)" stroke-width=".8" fill="none"/>
  </svg>
  <div class="label__ribbon"><span>NEW</span></div>
  <div class="brand"><span class="brand__dot"></span><span class="brand__name">Dorvalix</span></div>
  <div class="claims">
    <p class="claims__small">CLEANS</p>
    <p class="claims__main">DESCALES</p>
    <p class="claims__sub">FRESHENS</p>
  </div>
  <div class="label__visual" role="img" aria-label="Photo of a clean bathroom with toilet, washbasin and scrubbing brush"></div>
  <ul class="usps"><li>SANITARY</li><li>BATHROOM</li><li>TOILET</li><li>WET AREAS</li></ul>
  <div class="volume">1L</div>
  <p class="tagline">Ideal for quick and powerful cleaning.<br>A ready-to-use product for everyday use.</p>
  <svg class="label__water" viewBox="0 0 100 20" preserveAspectRatio="none" aria-hidden="true">
    <path d="M0 8C20 2 40 12 60 6S90 4 100 7V20H0Z" fill="var(--blue-pale)"/>
    <path d="M0 12C25 7 45 15 70 10S92 9 100 11V20H0Z" fill="var(--blue-soft)" opacity=".6"/>
  </svg>
</article>

<article class="label label--500" aria-label="Dorvalix sanitary cleaner, 500 ml spray label">
  <svg class="label__panel" viewBox="0 0 100 100" preserveAspectRatio="none" aria-hidden="true">
    <defs>
      <linearGradient id="panelBlue2" x1="0" y1="0" x2="1" y2="1">
        <stop offset="0" stop-color="var(--blue-deep)"/>
        <stop offset=".6" stop-color="var(--blue-mid)"/>
        <stop offset="1" stop-color="var(--blue-deep)"/>
      </linearGradient>
    </defs>
    <path d="M0 0H100V42C80 48 50 52 0 72Z" fill="url(#panelBlue2)"/>
    <path d="M0 74C40 55 75 50 100 44V48C75 53 40 58 0 78Z" fill="var(--blue-pale)"/>
    <path d="M0 70C45 52 78 47 100 41" stroke="var(--white)" stroke-width=".8" fill="none"/>
  </svg>
  <div class="label__ribbon"><span>NEW</span></div>
  <div class="brand"><span class="brand__dot"></span><span class="brand__name">Dorvalix</span></div>
  <div class="claims">
    <p class="claims__small">CLEANS</p>
    <p class="claims__main">DESCALES</p>
    <p class="claims__sub">FRESHENS</p>
  </div>
  <div class="label__visual" role="img" aria-label="Photo of a clean bathroom with toilet, washbasin and scrubbing brush"></div>
  <ul class="usps"><li>SANITARY</li><li>BATHROOM</li><li>TOILET</li><li>WET AREAS</li></ul>
  <div class="volume">500ml</div>
  <p class="tagline">Ideal for quick and powerful cleaning.<br>A ready-to-use product for everyday use.</p>
  <svg class="label__water" viewBox="0 0 100 20" preserveAspectRatio="none" aria-hidden="true">
    <path d="M0 8C20 2 40 12 60 6S90 4 100 7V20H0Z" fill="var(--blue-pale)"/>
    <path d="M0 12C25 7 45 15 70 10S92 9 100 11V20H0Z" fill="var(--blue-soft)" opacity=".6"/>
  </svg>
</article>

</body>
</html>
```